Business Card needed for Drainor, a growing Septic Service company

Drainor, a growing local septic service company in Pennsylvania, needs updated business cards. We'd like the business card to feature our logo and communicate that we provide Septic Pumping, Installations/Repairs, Restroom Rentals, and 24/7 Emergency Service. The business card should be eye-catching, bold, and clean/simple. We have been in business almost 10 years and would like to expand and update our business brand and image.

Target Market(s)

Residential and Commercial, New and Current Homeowners

Industry/Entity Type

Service

Contact Information for Business Card

Contact on the business card should be: Dean Harlow Owner & Operator
Phone: 555-555-0187
Email: service@drainor-example.com
Website: www.drainor-example.com
Address: 812 Millbrook Lane Riverton PA 00000

Font styles to use
Sans Serif

Colors

Designer to choose colors to be used in the design.

Requirements
Must have
• Feature logo on both side of business card.
Nice to have
• We envision the contact information on one side and our services listed on the other side. Utilize the green from the symbol in our logo as part of the design, overall design color scheme should be white, grey, black.

```html
<!DOCTYPE html>
<html lang="en">
<head>
<meta charset="utf-8">
<title>Drainor Business Card Concepts</title>
<link rel="stylesheet" href="https://fonts.googleapis.com/css2?family=Montserrat:wght@500;800&family=Oswald:wght@500&family=Lexend:wght@300;400&display=swap">
<style>
  :root {
    --green: #8dc63f;
    --green-deep: #6f9e36;
    --lime: #d9e36a;
    --yellow: #f7ef7a;
    --ink: #111111;
    --grey: #d7d7d7;
    --page: #f4f6f9;
    --panel: #eef1f5;
    --white: #ffffff;
    --label: #8a8f96;
  }
  * { margin: 0; padding: 0; box-sizing: border-box; }
  html, body { width: 1200px; height: 680px; overflow: hidden; background: var(--page); }
  body { position: relative; font-family: "Lexend", sans-serif; color: var(--ink); }

  .panel { position: absolute; background: var(--panel); }
  .panel--upper { left: 155px; top: 19px; width: 591px; height: 432px; }
  .panel--lower { left: 463px; top: 240px; width: 579px; height: 432px; }

  .card {
    position: absolute; width: 266px; height: 152px; overflow: hidden;
    background: var(--white); box-shadow: 0 1px 4px rgba(0,0,0,0.12);
  }
  .card > * { position: absolute; }
  .card-number {
    position: absolute; width: 266px; text-align: center;
    font-family: "Lexend", sans-serif; font-size: 14px; color: var(--label);
  }

  .logo { display: flex; align-items: center; gap: 4px; white-space: nowrap; }
  .logo-mark { width: 11px; height: 11px; background: var(--green); }
  .logo-name {
    font-family: "Montserrat", sans-serif; font-weight: 800; font-size: 16px;
    letter-spacing: 0.5px; color: var(--ink); line-height: 1;
  }

  .center { left: 0; width: 100%; text-align: center; }
  .centered-logo { left: 50%; transform: translateX(-50%); }
  .tiny { font-size: 5px; line-height: 7.2px; letter-spacing: 0.3px; white-space: nowrap; }
  .small { font-size: 6.5px; line-height: 10px; letter-spacing: 0.2px; white-space: nowrap; }

  .wave-band { left: 0; bottom: 0; width: 100%; height: 34px; }

  /* card 3 */
  .c3-top { left: 0; top: 0; width: 100%; height: 42px; background: var(--white); }
  .c3-body { left: 0; top: 42px; width: 100%; height: 110px; background: var(--green); }
  .c3-name { top: 53px; font-family: "Montserrat", sans-serif; font-weight: 800; font-size: 12px; color: var(--white); letter-spacing: 0.3px; }
  .c3-role { top: 71px; font-size: 5.5px; color: var(--white); }
  .c3-contact { top: 83px; color: var(--white); }
  .c3-waves { background: linear-gradient(180deg, #b9dd8c 0%, #a6d46f 100%); }
  .c4-waves { background: linear-gradient(180deg, #ffffff 0%, #cfe8ac 100%); }

  /* card 7 */
  .c7 { background: var(--green); }
  .c7-circle { left: -34px; top: 13px; width: 124px; height: 124px; border-radius: 50%; background: var(--ink); }
  .c7-logo-band { left: 133px; top: 18px; width: 133px; height: 28px; background: var(--white); }
  .c7-name { right: 13px; top: 56px; font-family: "Oswald", sans-serif; font-weight: 500; font-size: 18px; color: var(--ink); line-height: 1; white-space: nowrap; }
  .c7-role { right: 13px; top: 88px; font-size: 5px; color: #2b3a1c; white-space: nowrap; }
  .c7-services { right: 13px; top: 110px; text-align: right; color: #2b3a1c; }

  /* card 1 and 2 */
  .shapes { left: 0; top: 0; width: 266px; height: 152px; }
  .dots { background: rgba(255,255,255,0.4); }
  .c1-services { right: 21px; top: 17px; text-align: right; font-size: 6.8px; line-height: 11px; color: #333; white-space: nowrap; }
  .c2-box { left: 27px; top: 18px; width: 212px; height: 114px; background: var(--grey); }
  .c2-title { top: 71px; font-size: 5px; color: #222; letter-spacing: 0.4px; }
  .c2-contact { top: 86px; color: #333; }

  /* card 5 */
  .c5-name { top: 62px; font-size: 15px; font-weight: 400; color: var(--green); letter-spacing: 0.5px; }
  .c5-role { top: 83px; font-size: 6px; color: var(--green); }
  .c5-contact { top: 96px; color: #222; }

  /* card 6 */
  .c6-side { left: 0; top: 0; width: 62px; height: 152px; background: linear-gradient(180deg, var(--green) 0%, #a9d77a 45%, var(--green-deep) 100%); }
  .c6-name { left: 114px; top: 70px; font-size: 9.5px; color: #333; letter-spacing: 0.2px; white-space: nowrap; }
  .c6-role { left: 114px; top: 83px; font-size: 4.2px; color: #777; font-style: italic; letter-spacing: 0.4px; white-space: nowrap; }
  .c6-contact { left: 114px; top: 100px; font-size: 4.6px; line-height: 9.6px; color: #555; font-weight: 300; white-space: nowrap; }
</style>
</head>
<body>
  <div class="panel panel--upper"></div>
  <div class="panel panel--lower"></div>

  <section class="card" style="left:172px; top:30px;">
    <div class="c3-top"></div>
    <div class="c3-body"></div>
    <div class="logo centered-logo" style="top:14px;"><span class="logo-mark"></span><span class="logo-name">DRAINOR</span></div>
    <p class="center c3-name">DEAN HARLOW</p>
    <p class="center c3-role">Owner and Operator</p>
    <p class="center tiny c3-contact">Phone: 555-555-0187<br>Email: service@drainor-example.com<br>Website: www.drainor-example.com<br>Address: 812 Millbrook Lane Riverton PA 00000</p>
    <div class="wave-band c3-waves" role="img" aria-label="Wavy green and white water-line pattern"></div>
  </section>
  <p class="card-number" style="left:172px; top:190px;">3</p>

  <section class="card" style="left:467px; top:30px;">
    <div class="logo centered-logo" style="top:48px;"><span class="logo-mark"></span><span class="logo-name">DRAINOR</span></div>
    <p class="center small" style="top:75px; color:#222;">Septic Pumping | Installations/Repairs<br>Restroom Rentals | 24/7 Emergency Service</p>
    <div class="wave-band c4-waves" role="img" aria-label="Wavy green water-line pattern"></div>
  </section>
  <p class="card-number" style="left:467px; top:190px;">4</p>

  <section class="card c7" style="left:172px; top:251px;">
    <div class="c7-circle" role="img" aria-label="Large black circle brand accent"></div>
    <div class="c7-logo-band"></div>
    <div class="logo" style="left:144px; top:26px;"><span class="logo-mark"></span><span class="logo-name">DRAINOR</span></div>
    <p class="c7-name">DEAN HARLOW</p>
    <p class="c7-role">Owner and Operator</p>
    <p class="tiny c7-services">Septic Pumping | Installations/Repairs<br>Restroom Rentals | 24/7 Emergency Service</p>
  </section>
  <p class="card-number" style="left:172px; top:411px;">7</p>

  <section class="card" style="left:467px; top:251px; background:var(--yellow);">
    <svg class="shapes" viewBox="0 0 266 152" aria-hidden="true">
      <polygon points="0,112 126,57 160,152 0,152" fill="var(--white)"/>
      <polygon points="126,57 266,0 266,152 160,152" fill="var(--lime)"/>
    </svg>
    <div class="dots" style="left:22px; top:4px; width:48px; height:32px;" role="img" aria-label="Dot grid texture"></div>
    <div class="dots" style="left:197px; top:118px; width:48px; height:30px;" role="img" aria-label="Dot grid texture"></div>
    <p class="c1-services">Septic Pumping | Installations/Repairs<br>Restroom Rentals | 24/7 Emergency Service</p>
    <div class="logo" style="left:32px; top:114px;"><span class="logo-mark"></span><span class="logo-name">DRAINOR</span></div>
  </section>
  <p class="card-number" style="left:467px; top:411px;">1</p>

  <section class="card" style="left:763px; top:251px;">
    <svg class="shapes" viewBox="0 0 266 152" aria-hidden="true">
      <polygon points="40,0 266,0 266,152 210,152" fill="var(--yellow)"/>
      <polygon points="88,152 200,60 266,140 266,152" fill="var(--lime)"/>
    </svg>
    <div class="dots" style="left:178px; top:0; width:50px; height:22px;" role="img" aria-label="Dot grid texture"></div>
    <div class="c2-box"></div>
    <div class="dots" style="left:95px; top:128px; width:50px; height:22px;" role="img" aria-label="Dot grid texture"></div>
    <div class="logo centered-logo" style="top:41px;"><span class="logo-mark"></span><span class="logo-name">DRAINOR</span></div>
    <p class="center c2-title">Dean Harlow | Owner &amp; Operator</p>
    <p class="center tiny c2-contact">Phone: 555-555-0187<br>Email: service@drainor-example.com<br>Website: www.drainor-example.com<br>Address: 812 Millbrook Lane Riverton PA 00000</p>
  </section>
  <p class="card-number" style="left:763px; top:411px;">2</p>

  <section class="card" style="left:467px; top:470px;">
    <div class="logo centered-logo" style="top:32px;"><span class="logo-mark"></span><span class="logo-name">DRAINOR</span></div>
    <p class="center c5-name">DEAN HARLOW</p>
    <p class="center c5-role">Owner and Operator</p>
    <p class="center tiny c5-contact">Phone: 555-555-0187<br>Email: service@drainor-example.com<br>Website: www.drainor-example.com<br>Address: 812 Millbrook Lane Riverton PA 00000</p>
  </section>
  <p class="card-number" style="left:467px; top:630px;">5</p>

  <section class="card" style="left:763px; top:470px;">
    <div class="c6-side" role="img" aria-label="Green panel with layered water drop illustration"></div>
    <div class="logo" style="left:114px; top:18px;"><span class="logo-mark"></span><span class="logo-name">DRAINOR</span></div>
    <p class="c6-name">DEAN HARLOW</p>
    <p class="c6-role">OWNER AND OPERATOR</p>
    <p class="c6-contact">Phone: 555-555-0187<br>Email: service@drainor-example.com<br>Website: www.drainor-example.com<br>Address: 812 Millbrook Lane Riverton PA 00000</p>
  </section>
  <p class="card-number" style="left:763px; top:630px;">6</p>
</body>
</html>
```